Roofing company in Toronto, Canada needs a logo design and business card design

We need a business card and logo created for our company. Our company is "KVL Roofing" which provides roofing services for commercial and residential customers. We serve customers in the Greater Toronto Area (in Canada) thus the name KVL.

We want the logo and business card to be a modern design displaying professionalism and quality in the work. We would prefer rounded corners for the business cards but are open to other ideas. The cards should be pleasant and appealing to customers.

Target Market(s)

Commercial and Residential customers

Industry/Entity Type

Roofing

Contact Information for Business Card

Logo Text

KVL Roofing

Requirements
Nice to have
• Colours that are pleasing to the eye but at the same time should stand out from other business cards. If the design can incorporate the name of KVL Roofing and the actual concept of roofing that would be nice.
Should not have
• Do not want the business cards or logo to be childish looking. Need to look professionally designed.

```html
<!DOCTYPE html>
<html lang="en">
<head>
<meta charset="utf-8">
<title>KVL Roofing – Business Card</title>
<link href="https://fonts.googleapis.com/css2?family=Lato:wght@400;700;900&display=swap" rel="stylesheet">
<style>
  :root {
    --stage: #3a3430;
    --card-dark: #0b0b0b;
    --card-light: #ffffff;
    --brand-red: #e3202a;
    --ink: #1a1a1a;
    --rule: #9a9a9a;
    --band-edge: #c9c9c9;
  }
  * { box-sizing: border-box; margin: 0; padding: 0; }
  html, body { width: 1200px; height: 780px; overflow: hidden; }
  body {
    background: var(--stage);
    font-family: "Lato", sans-serif;
    position: relative;
  }
  .card {
    position: absolute;
    width: 530px;
    height: 303px;
    border-radius: 10px;
    overflow: hidden;
    box-shadow: 0 12px 30px rgba(0,0,0,.45);
  }
  .card--front { left: 45px; top: 238px; background: var(--card-dark); }
  .card--back { left: 625px; top: 238px; background: var(--card-light); }

  .wordmark {
    display: flex;
    align-items: center;
    gap: 12px;
    font-weight: 900;
    letter-spacing: 1px;
  }
  .wordmark__dot {
    width: 16px; height: 16px; border-radius: 50%;
    background: var(--brand-red);
  }
  .card--front .wordmark {
    position: absolute; left: 0; right: 0; top: 0; bottom: 0;
    justify-content: center;
    color: #ffffff;
    font-size: 40px;
  }
  .card--back .wordmark {
    position: absolute; left: 40px; top: 100px;
    color: var(--ink);
    font-size: 30px;
  }
  .divider {
    position: absolute; left: 262px; top: 70px;
    width: 1px; height: 140px; background: #333;
  }
  .person { position: absolute; left: 290px; top: 80px; }
  .person__name {
    font-size: 20px; font-weight: 900; color: var(--ink);
    text-transform: uppercase; letter-spacing: .5px;
  }
  .person__title { font-size: 15px; color: var(--brand-red); margin-top: -2px; }
  .contact { position: absolute; left: 290px; top: 140px; list-style: none; }
  .contact li {
    display: flex; align-items: center; gap: 8px;
    font-size: 14px; color: var(--ink); line-height: 19px;
  }
  .contact .icon {
    width: 14px; height: 14px; background: var(--brand-red);
    border-radius: 2px; flex: none;
  }
  .contact .icon svg { display: block; }
  .contact li.web .icon { visibility: hidden; }
  .band-rule {
    position: absolute; left: 0; right: 0; bottom: 55px;
    height: 3px; background: var(--band-edge);
  }
  .address-band {
    position: absolute; left: 0; right: 0; bottom: 0;
    height: 50px; background: var(--brand-red);
    color: #ffffff; font-size: 14px;
    display: flex; align-items: center; padding-left: 40px;
  }
</style>
</head>
<body>
  <section class="card card--front" aria-label="Card front">
    <div class="wordmark"><span class="wordmark__dot"></span>KVL Roofing</div>
  </section>

  <section class="card card--back" aria-label="Card back">
    <div class="wordmark"><span class="wordmark__dot"></span>KVL Roofing</div>
    <div class="divider"></div>
    <div class="person">
      <p class="person__name">Daniel Reyes</p>
      <p class="person__title">Managing Director</p>
    </div>
    <ul class="contact">
      <li><span class="icon"><svg width="14" height="14" viewBox="0 0 14 14"><path d="M4 3h2l1 2-1 1a5 5 0 0 0 2 2l1-1 2 1v2c-4 0-7-3-7-7z" fill="#fff"/></svg></span>(01) 5550 1820</li>
      <li><span class="icon"><svg width="14" height="14" viewBox="0 0 14 14"><rect x="3" y="5" width="8" height="5" fill="#fff"/><rect x="4.5" y="3" width="5" height="2" fill="#fff"/></svg></span>(01) 5550 1821</li>
      <li><span class="icon"><svg width="14" height="14" viewBox="0 0 14 14"><rect x="3" y="4" width="8" height="6" fill="#fff"/><path d="M3 4l4 3 4-3" stroke="#e3202a" fill="none"/></svg></span>info@kvlroof.com</li>
      <li><span class="icon"><svg width="14" height="14" viewBox="0 0 14 14"><circle cx="7" cy="7" r="4" fill="none" stroke="#fff"/><path d="M3 7h8M7 3v8" stroke="#fff"/></svg></span>www.kvlroof.com</li>
    </ul>
    <div class="band-rule"></div>
    <div class="address-band">PO BOX 480 Harbour Lane, 2nd street Toronto, CA</div>
  </section>
</body>
</html>
```